Ironvale Holdings Business card

We need a an amazing matte black and gold card! W are a finance investing company so we want something that's eye catching and sleek. We want it to be attractive and sleek and represent money. Heck with would like the letters and lgo to be printed as 24k gold one day. We have the logo added so please use the color scheme with the logo and have that beautifully placed on one side.

Target Market(s)

Investors of all ages

Industry/Entity Type

Financial

Contact Information for Business Card

Black and matte with gold lettering follow logo colrs please.

Font styles to use
Other font styles liked:
• you decide

Colors

Designer to choose colors to be used in the design.

Requirements
Must have
• Matte Black and Gold, logo on one side. job title and name , website, phone number and email address on the other side
Nice to have
• Matte black and crisp finish to attract investors
Should not have
• playful, very professional!

```html
<!DOCTYPE html>
<html lang="en">
<head>
<meta charset="UTF-8">
<title>Ironvale Holdings Business Card</title>
<link href="https://fonts.googleapis.com/css2?family=Cinzel:wght@700&family=Lato:wght@400&display=swap" rel="stylesheet">
<style>
  :root {
    --backdrop: #2a2c30;
    --card-black: #0d0d0e;
    --card-edge: #1c1c1e;
    --gold: #d9b533;
    --gold-soft: #b8962a;
    --contact-text: #e6e6e6;
  }
  * { box-sizing: border-box; margin: 0; padding: 0; }
  html, body {
    width: 1200px;
    height: 900px;
    overflow: hidden;
    background: var(--backdrop);
  }
  .canvas {
    width: 1200px;
    height: 900px;
    display: flex;
    flex-direction: column;
    align-items: center;
    justify-content: center;
    gap: 56px;
  }
  .card {
    width: 630px;
    height: 360px;
    background: var(--card-black);
    border: 1px solid var(--card-edge);
    box-shadow: 0 14px 30px rgba(0, 0, 0, 0.45);
    position: relative;
  }
  .brand-name {
    font-family: "Lato", sans-serif;
    font-weight: 400;
    color: var(--gold);
    text-align: center;
    white-space: nowrap;
  }

  /* Logo side */
  .card--front {
    display: flex;
    align-items: center;
    justify-content: center;
  }
  .card--front .brand-name {
    font-size: 40px;
  }

  /* Contact side */
  .card--back .brand-name {
    position: absolute;
    top: 74px;
    left: 0;
    right: 0;
    font-size: 32px;
  }
  .details {
    position: absolute;
    left: 0;
    right: 0;
    bottom: 58px;
    display: flex;
    justify-content: center;
    align-items: center;
  }
  .person {
    text-align: right;
    padding-right: 26px;
  }
  .person__name {
    font-family: "Cinzel", serif;
    font-weight: 700;
    font-size: 20px;
    color: var(--gold);
    letter-spacing: 0.02em;
  }
  .person__title {
    font-family: "Lato", sans-serif;
    font-size: 15px;
    color: var(--gold-soft);
    margin-top: 4px;
  }
  .divider {
    width: 1px;
    height: 92px;
    background: linear-gradient(to bottom, transparent, var(--gold-soft), transparent);
  }
  .contacts {
    list-style: none;
    padding-left: 26px;
  }
  .contacts li {
    display: flex;
    align-items: center;
    gap: 10px;
    font-family: "Lato", sans-serif;
    font-size: 16px;
    color: var(--contact-text);
    line-height: 1.65;
  }
  .contacts svg {
    width: 15px;
    height: 15px;
    flex: none;
  }
</style>
</head>
<body>
<main class="canvas">
  <section class="card card--front">
    <p class="brand-name">Ironvale Holdings</p>
  </section>

  <section class="card card--back">
    <p class="brand-name">Ironvale Holdings</p>
    <div class="details">
      <div class="person">
        <p class="person__name">MARCUS HALE</p>
        <p class="person__title">Director/ CEO</p>
      </div>
      <div class="divider"></div>
      <ul class="contacts">
        <li>
          <svg viewBox="0 0 16 16" aria-hidden="true">
            <circle cx="8" cy="8" r="7" fill="none" stroke="#d9b533" stroke-width="1.4"/>
            <path d="M5.6 4.6l1.2 1.6-.7.9c.5 1 1.3 1.8 2.3 2.3l.9-.7 1.6 1.2-.6 1.2c-2.9-.3-5.1-2.5-5.4-5.4z" fill="#d9b533"/>
          </svg>
          0123 555 018
        </li>
        <li>
          <svg viewBox="0 0 16 16" aria-hidden="true">
            <rect x="1.5" y="3.5" width="13" height="9" fill="none" stroke="#d9b533" stroke-width="1.4"/>
            <path d="M1.5 3.5L8 9l6.5-5.5" fill="none" stroke="#d9b533" stroke-width="1.4"/>
          </svg>
          info@ironvaleholdings.com
        </li>
        <li>
          <svg viewBox="0 0 16 16" aria-hidden="true">
            <circle cx="8" cy="8" r="6.5" fill="none" stroke="#d9b533" stroke-width="1.4"/>
            <ellipse cx="8" cy="8" rx="2.8" ry="6.5" fill="none" stroke="#d9b533" stroke-width="1.1"/>
            <path d="M1.5 8h13M2.6 4.8h10.8M2.6 11.2h10.8" stroke="#d9b533" stroke-width="1.1"/>
          </svg>
          www.ironvaleholdings.com
        </li>
      </ul>
    </div>
  </section>
</main>
</body>
</html>
```